Quorvex - Automated robotic Inspection with AI need new business cards

We need a new design of our business cards. The company is focused on automated quality control at high speed with unmatched results. We have a logo but need a more forward leaning business card that shows that we are delivering cutting edge technology.

Contact Information for Business Card

Name
Position
Adress
Phone
Email
e.g.
Lena Holmqvist
Chief Financial Officer (CFO)

Quorvex Sweden AB
Bruksvägen 14, SE-175 43 JÄRFÄLLA, Sweden
Mobile: +46735 21 47 83 | Office: +46 8 61 94 27
www.quorvex-example.com

Font styles to use
Sans Serif

```html
<!DOCTYPE html>
<html lang="en">
<head>
<meta charset="utf-8">
<title>Quorvex Business Cards</title>
<link rel="stylesheet" href="https://fonts.googleapis.com/css2?family=Lato:wght@400;700;900&display=swap">
<style>
  :root {
    --brand-blue: #1b5a8b;
    --ink: #1c1c1c;
    --paper: #ffffff;
    --paper-tint: #f1f1f1;
    --backdrop: #232323;
  }
  * { box-sizing: border-box; margin: 0; padding: 0; }
  html, body { width: 857px; height: 1200px; overflow: hidden; }
  body {
    background: var(--backdrop);
    font-family: "Lato", sans-serif;
    display: flex;
    flex-direction: column;
    justify-content: space-around;
    padding: 60px 0;
  }
  .card-set {
    display: flex;
    flex-direction: column;
    align-items: center;
    gap: 28px;
  }
  .card-row { display: flex; gap: 28px; }
  .card {
    position: relative;
    width: 380px;
    height: 217px;
    border-radius: 16px;
    overflow: hidden;
  }
  /* Card backs */
  .card-back {
    display: flex;
    align-items: center;
    justify-content: center;
    gap: 14px;
  }
  .card-back--light { background: var(--paper-tint); color: var(--brand-blue); }
  .card-back--dark { background: var(--brand-blue); color: var(--paper); }
  .brand-mark {
    width: 34px; height: 34px;
    border-radius: 50%;
    background: currentColor;
  }
  .brand-name {
    font-weight: 900;
    font-size: 42px;
    letter-spacing: 2px;
    text-transform: uppercase;
  }
  /* Card front */
  .card-front { background: var(--paper); color: var(--ink); }
  .front-decoration {
    position: absolute;
    right: -70px; top: -60px;
    width: 220px; height: 220px;
    border-radius: 50%;
    background: var(--brand-blue);
  }
  .holder { position: absolute; left: 26px; top: 42px; }
  .holder-name {
    color: var(--brand-blue);
    font-weight: 900;
    font-size: 17px;
    letter-spacing: 1px;
    text-transform: uppercase;
  }
  .holder-title { font-size: 9.5px; margin-top: 2px; }
  .contact-list {
    position: absolute;
    left: 26px; top: 118px;
    list-style: none;
    font-size: 9px;
    line-height: 1.25;
  }
  .contact-item { display: flex; align-items: center; gap: 7px; margin-bottom: 5px; }
  .contact-icon {
    flex: none;
    width: 12px; height: 12px;
    border-radius: 50%;
    background: var(--brand-blue);
    display: flex; align-items: center; justify-content: center;
  }
  .contact-icon svg { width: 7px; height: 7px; fill: var(--paper); }
  .front-brand {
    position: absolute;
    right: 22px; bottom: 26px;
    display: flex; align-items: center; gap: 6px;
    color: var(--brand-blue);
  }
  .front-brand .brand-mark { width: 13px; height: 13px; }
  .front-brand .brand-name { font-size: 18px; letter-spacing: 1px; }
</style>
</head>
<body>

<section class="card-set">
  <div class="card-row">
    <article class="card card-back card-back--light">
      <span class="brand-mark"></span><span class="brand-name">Quorvex</span>
    </article>
    <article class="card card-front">
      <div class="front-decoration" role="img" aria-label="Large brand decoration in blue"></div>
      <div class="holder">
        <h2 class="holder-name">Lena Holmqvist</h2>
        <p class="holder-title">Chief Financial Officer (CFO)</p>
      </div>
      <ul class="contact-list">
        <li class="contact-item"><span class="contact-icon"><svg viewBox="0 0 10 10"><path d="M5 0a3.5 3.5 0 0 0-3.5 3.5C1.5 6 5 10 5 10s3.5-4 3.5-6.5A3.5 3.5 0 0 0 5 0zm0 5a1.4 1.4 0 1 1 0-2.8A1.4 1.4 0 0 1 5 5z"/></svg></span><span>Bruksvägen 14, SE-175 43<br>JÄRFÄLLA, Sweden</span></li>
        <li class="contact-item"><span class="contact-icon"><svg viewBox="0 0 10 10"><path d="M2 0l2 2.5-1 1.2a6 6 0 0 0 3.3 3.3l1.2-1L10 8l-1.5 2C4 10 0 6 0 1.5z"/></svg></span><span>+46735 21 47 83</span></li>
        <li class="contact-item"><span class="contact-icon"><svg viewBox="0 0 10 10"><path d="M2 0l2 2.5-1 1.2a6 6 0 0 0 3.3 3.3l1.2-1L10 8l-1.5 2C4 10 0 6 0 1.5z"/></svg></span><span>+46 8 61 94 27</span></li>
        <li class="contact-item"><span class="contact-icon"><svg viewBox="0 0 10 10"><path d="M0 2h10v6H0zM0 2l5 3.5L10 2v1L5 6.5 0 3z"/></svg></span><span>yourmailaddress@goeshere</span></li>
        <li class="contact-item"><span class="contact-icon"><svg viewBox="0 0 10 10"><path d="M5 0a5 5 0 1 0 0 10A5 5 0 0 0 5 0zm0 1a4 4 0 0 1 0 8 4 4 0 0 1 0-8zM1 4.5h8v1H1zM4.5 1h1v8h-1z"/></svg></span><span>www.quorvex-example.com</span></li>
      </ul>
      <div class="front-brand"><span class="brand-mark"></span><span class="brand-name">Quorvex</span></div>
    </article>
  </div>
</section>

<section class="card-set">
  <div class="card-row">
    <article class="card card-back card-back--dark">
      <span class="brand-mark"></span><span class="brand-name">Quorvex</span>
    </article>
    <article class="card card-front">
      <div class="front-decoration" role="img" aria-label="Large brand decoration in blue"></div>
      <div class="holder">
        <h2 class="holder-name">Lena Holmqvist</h2>
        <p class="holder-title">Chief Financial Officer (CFO)</p>
      </div>
      <ul class="contact-list">
        <li class="contact-item"><span class="contact-icon"><svg viewBox="0 0 10 10"><path d="M5 0a3.5 3.5 0 0 0-3.5 3.5C1.5 6 5 10 5 10s3.5-4 3.5-6.5A3.5 3.5 0 0 0 5 0zm0 5a1.4 1.4 0 1 1 0-2.8A1.4 1.4 0 0 1 5 5z"/></svg></span><span>Bruksvägen 14, SE-175 43<br>JÄRFÄLLA, Sweden</span></li>
        <li class="contact-item"><span class="contact-icon"><svg viewBox="0 0 10 10"><path d="M2 0l2 2.5-1 1.2a6 6 0 0 0 3.3 3.3l1.2-1L10 8l-1.5 2C4 10 0 6 0 1.5z"/></svg></span><span>+46735 21 47 83</span></li>
        <li class="contact-item"><span class="contact-icon"><svg viewBox="0 0 10 10"><path d="M2 0l2 2.5-1 1.2a6 6 0 0 0 3.3 3.3l1.2-1L10 8l-1.5 2C4 10 0 6 0 1.5z"/></svg></span><span>+46 8 61 94 27</span></li>
        <li class="contact-item"><span class="contact-icon"><svg viewBox="0 0 10 10"><path d="M0 2h10v6H0zM0 2l5 3.5L10 2v1L5 6.5 0 3z"/></svg></span><span>yourmailaddress@goeshere</span></li>
        <li class="contact-item"><span class="contact-icon"><svg viewBox="0 0 10 10"><path d="M5 0a5 5 0 1 0 0 10A5 5 0 0 0 5 0zm0 1a4 4 0 0 1 0 8 4 4 0 0 1 0-8zM1 4.5h8v1H1zM4.5 1h1v8h-1z"/></svg></span><span>www.quorvex-example.com</span></li>
      </ul>
      <div class="front-brand"><span class="brand-mark"></span><span class="brand-name">Quorvex</span></div>
    </article>
  </div>
</section>

</body>
</html>
```